New Architectural Firm Business Cards

New Business card to compliment previous pixel harbor logo (attached). Please design a business card that is simple, modern, creative....please do not use "symbols", simply the logo and associated graphics/text. The front should contain name/address/phone/email/web address (with graphics).....back should be 100% graphic design using the logo somehow. Hoping for a two color (black and yellow) design. full bleed design, no borders

Target Market(s)

Commercial Architecture Clients

Industry/Entity Type

Architecture

Contact Information for Business Card

Please design a business card that is simple, modern, creative....please do not use "symbols", simply the logo and associated graphics/text. The front should contain name/address/phone/email/web address (with graphics).....back should be 100% graphic design using the logo somehow

Font styles to use
Sans Serif

Colors
FFF300
FFF600
FEFA6F
FFFEC7
FFFEE8

Requirements
Must have
• Clean, Modern Design
Should not have
• Stock images or "icons"

```html
<!DOCTYPE html>
<html lang="en">
<head>
<meta charset="utf-8">
<title>Pixel Harbor Business Card</title>
<link href="https://fonts.googleapis.com/css2?family=Open+Sans:ital,wght@0,400;0,700;1,400&display=swap" rel="stylesheet">
<style>
  :root {
    --backdrop: #2e2826;
    --card-black: #141414;
    --brand-yellow: #f5c116;
    --text-white: #ffffff;
    --pattern-dark: #1c1c1c;
    --pattern-mid: #3a3a3a;
  }
  * { margin: 0; padding: 0; box-sizing: border-box; }
  html, body {
    width: 1200px; height: 847px; overflow: hidden;
    background: var(--backdrop);
    font-family: "Open Sans", Arial, sans-serif;
  }
  .stage { position: relative; width: 1200px; height: 847px; }
  .card {
    position: absolute; top: 269px;
    width: 540px; height: 309px;
    background: var(--card-black);
    overflow: hidden;
  }
  .card-back { left: 40px; }
  .card-front { left: 620px; }

  /* back side */
  .brand-pattern {
    position: absolute; inset: 0;
    background: linear-gradient(150deg, var(--pattern-dark) 0%, var(--card-black) 45%, var(--pattern-mid) 100%);
  }
  .back-mark {
    position: absolute; left: 50%; top: 58%;
    transform: translate(-50%, -50%);
    color: var(--brand-yellow);
    font-weight: 700; font-size: 26px; letter-spacing: 0.5px;
  }

  /* front side */
  .tab-accent {
    position: absolute; left: -14px; top: 40px;
    width: 28px; height: 28px; border-radius: 50%;
    background: var(--brand-yellow);
  }
  .person { position: absolute; left: 36px; top: 38px; }
  .person-name {
    color: var(--brand-yellow); font-weight: 700; font-size: 24px;
    text-transform: uppercase; line-height: 1.1;
  }
  .person-title {
    color: var(--text-white); font-style: italic; font-size: 16px;
  }
  .contact-list {
    position: absolute; left: 36px; top: 122px; list-style: none;
  }
  .contact-list li {
    display: flex; align-items: center; gap: 8px;
    color: var(--text-white); font-size: 16px; line-height: 27px;
  }
  .contact-list svg { width: 13px; height: 13px; fill: var(--brand-yellow); flex: none; }
  .firm-name {
    position: absolute; right: 40px; top: 132px;
    color: var(--brand-yellow); font-weight: 700; font-size: 30px;
    text-transform: uppercase; letter-spacing: 0.5px;
  }
  .address {
    position: absolute; right: 40px; bottom: 30px;
    color: var(--text-white); font-size: 16px; line-height: 26px; text-align: right;
  }
</style>
</head>
<body>
<main class="stage">
  <section class="card card-back">
    <div class="brand-pattern" role="img" aria-label="Tone-on-tone repeating brand pattern in dark greys"></div>
    <div class="back-mark">Pixel Harbor</div>
  </section>

  <section class="card card-front">
    <span class="tab-accent"></span>
    <div class="person">
      <div class="person-name">Elena Marsh</div>
      <div class="person-title">President</div>
    </div>
    <ul class="contact-list">
      <li>
        <svg viewBox="0 0 24 24"><path d="M6.6 10.8a15.1 15.1 0 0 0 6.6 6.6l2.2-2.2a1 1 0 0 1 1-.25 11.4 11.4 0 0 0 3.6.57 1 1 0 0 1 1 1V20a1 1 0 0 1-1 1A17 17 0 0 1 3 4a1 1 0 0 1 1-1h3.5a1 1 0 0 1 1 1c0 1.25.2 2.45.57 3.57a1 1 0 0 1-.25 1z"/></svg>
        555-210-4837
      </li>
      <li>
        <svg viewBox="0 0 24 24"><path d="M2 5h20v14H2z M2 5l10 8 10-8" /></svg>
        info@pixelharbor.com
      </li>
      <li>
        <svg viewBox="0 0 24 24"><circle cx="12" cy="12" r="10"/></svg>
        www.pixelharbor.com
      </li>
    </ul>
    <div class="firm-name">Pixel Harbor</div>
    <address class="address" style="font-style:normal">
      1180 Harbor Crest Way<br>
      Seaview Bay CA 90410
    </address>
  </section>
</main>
</body>
</html>
```